Attract renters to our neighborhoods - inform renters who we are

Apartments in several neighborhoods. We want to attract renters who want to live along the lake or other near by neighborhoods. We want them to know that we have an apartment for them in their location.
The perfect location to spend your time.
When minutes matter LIVE where you work and play! (love this tag line)
Updates

www.kvtresidences.example Choose from over 3,700 apartments in Chicago’s most celebrated neighborhoods. 773-582-6041 Chicago’s most celebrated neighborhoods. 31 PROPERTIES

Target Market(s)

Sophisticated apartment renter who wants location, space, amenities

Industry/Entity Type

Apartment Rentals

Requirements
Must have
• Feel like I want to live there, or the ad is calling me
Nice to have
• Appeal to a sophisticated apartment renter. We have what you want, where you want to be.
Should not have
• Logo colors are black and red/burnt orange see attached logo

```html
<!DOCTYPE html>
<html lang="en">
<head>
<meta charset="utf-8">
<title>KVT Residences – Flyer</title>
<link rel="stylesheet" href="https://fonts.googleapis.com/css2?family=Oswald:wght@400;500&family=Lato:wght@300;400;700;900&display=swap">
<style>
  :root {
    --red: #c50f2a;
    --charcoal: #2d2d2d;
    --white: #ffffff;
    --ink: #111111;
    --backdrop: #c9d0d9;
    --sky: #5f9fd6;
    --lake: #1e8c94;
    --city: #9a9a92;
    --cell: 258px;
    --gap: 14px;
  }
  * { box-sizing: border-box; margin: 0; padding: 0; }
  html, body {
    width: 1004px; height: 1200px; overflow: hidden;
    background: var(--backdrop);
  }
  .flyer {
    position: absolute; left: 72px; top: 34px;
    width: 860px; height: 1132px;
    background: var(--white);
    padding: 29px;
    display: grid;
    grid-template-columns: repeat(3, var(--cell));
    grid-template-rows: repeat(4, var(--cell));
    gap: var(--gap);
  }
  .tile {
    display: flex; align-items: center; justify-content: center;
    text-align: center;
  }
  .tile--red { background: var(--red); color: var(--white); }
  .tile--dark { background: var(--charcoal); color: var(--white); }
  .tagline {
    font-family: "Oswald", sans-serif; font-weight: 400;
    font-size: 38px; line-height: 1.18; text-transform: uppercase;
    letter-spacing: -0.3px;
  }
  .neighborhood {
    font-family: "Lato", sans-serif; font-weight: 400;
    font-size: 26px; line-height: 1.2; text-transform: uppercase;
  }
  .photo { width: 100%; height: 100%; }
  .photo--skyline { background: linear-gradient(180deg, var(--sky) 0%, #8fb7d8 25%, var(--city) 55%, var(--lake) 100%); }
  .photo--beach { background: linear-gradient(180deg, var(--sky) 0%, #a9c9e2 25%, #6f8f6a 45%, #e4d3b0 62%, var(--lake) 80%); }
  .photo--towers { background: linear-gradient(180deg, var(--sky) 0%, #2d86b8 35%, var(--city) 65%, #6d7f6a 100%); }
  .photo--harbor { background: linear-gradient(180deg, #8cb8de 0%, var(--city) 30%, #5d8a5e 55%, var(--lake) 100%); }

  .stats {
    grid-column: 2 / span 2;
    flex-direction: column;
    font-family: "Lato", sans-serif;
    text-transform: uppercase;
  }
  .stats__lead { font-size: 25px; font-weight: 400; margin-bottom: 8px; }
  .stats__figures { display: flex; align-items: stretch; }
  .figure { width: 252px; display: flex; flex-direction: column; align-items: center; }
  .figure__num { font-size: 48px; font-weight: 400; line-height: 1.05; }
  .figure__label { font-size: 28px; font-weight: 400; line-height: 1.1; }
  .stats__divider { width: 2px; background: var(--white); margin: 4px 0; }
  .stats__close { font-size: 26px; font-weight: 300; line-height: 1.22; margin-top: 16px; }
  .stats__close strong { font-weight: 700; }

  .brand {
    flex-direction: column; align-items: stretch; justify-content: flex-start;
    padding-top: 24px;
    font-family: "Lato", sans-serif;
  }
  .brand__name {
    font-weight: 900; font-size: 76px; color: var(--ink);
    letter-spacing: 2px; line-height: 1; text-align: center;
    margin: 6px 0 30px;
  }
  .brand__rule { height: 2px; background: var(--red); margin: 0 16px 20px 0; }
  .brand__web { color: var(--red); font-weight: 700; font-size: 18px; text-align: left; }
  .brand__phone {
    color: var(--red); font-weight: 700; font-size: 29px; text-align: left;
    display: flex; align-items: center; gap: 10px; margin-top: 6px;
  }
  .brand__phone svg { width: 20px; height: 20px; }
</style>
</head>
<body>
  <main class="flyer">
    <div class="tile tile--red"><p class="tagline">When minutes<br>matter live<br>where you<br>work &amp; play!</p></div>
    <div class="tile tile--dark"><p class="neighborhood">Gold Coast<br>&amp; Old Town</p></div>
    <div class="photo photo--skyline" role="img" aria-label="Aerial view of the downtown skyline along the lakefront"></div>

    <div class="photo photo--beach" role="img" aria-label="Aerial view of a curving city beach on the lake"></div>
    <div class="photo photo--towers" role="img" aria-label="Aerial view of high-rise towers beside the lake"></div>
    <div class="tile tile--dark"><p class="neighborhood">River<br>North</p></div>

    <div class="tile tile--dark"><p class="neighborhood">Lincoln<br>Park</p></div>
    <div class="tile tile--red stats">
      <p class="stats__lead">Choose from over</p>
      <div class="stats__figures">
        <div class="figure"><span class="figure__num">31</span><span class="figure__label">Properties</span></div>
        <div class="stats__divider"></div>
        <div class="figure"><span class="figure__num">3,700</span><span class="figure__label">Apartments</span></div>
      </div>
      <p class="stats__close">In Chicago’s most <strong>celebrated<br>neighborhoods.</strong></p>
    </div>

    <div class="tile brand">
      <p class="brand__name">KVT</p>
      <div class="brand__rule"></div>
      <p class="brand__web">www.kvtresidences.example</p>
      <p class="brand__phone">
        <svg viewBox="0 0 24 24" aria-hidden="true"><path fill="currentColor" d="M6.6 10.8a15.1 15.1 0 0 0 6.6 6.6l2.2-2.2c.3-.3.7-.4 1-.2 1.1.4 2.3.6 3.6.6.6 0 1 .4 1 1V20c0 .6-.4 1-1 1A17 17 0 0 1 3 4c0-.6.4-1 1-1h3.5c.6 0 1 .4 1 1 0 1.3.2 2.5.6 3.6.1.3 0 .7-.2 1z"/></svg>
        773-582-6041
      </p>
    </div>
    <div class="tile tile--dark"><p class="neighborhood">Lakeview</p></div>
    <div class="photo photo--harbor" role="img" aria-label="Aerial view of a lakefront harbor with moored boats"></div>
  </main>
</body>
</html>
```